Stonevale Business Card Design

The Stonevale Co is an aggregate (crushing) equipment dealer serving Western Canadian provinces. Stonevale is a distributor of aggregate equipment for different manufacturers.

We are looking to change and update the existing business card which has been used since the existence of the company. A copy of existing card has been attached for reference. The Stonevale Co logo we want to remain the same and we want the green color to remain the same.

We are wanting something new with a different look. A refreshing card to show a new modern and updated look. No longer wanting to have the manufacturers on the back of the card but something more like our logo on the back of the card with a statement like "Crushing Solutions"

ideas could be:
- card can be different colors on front and back
- front or reverse of the card could possibly be the green color with the logo in black

Target Market(s)

Owners of Aggregate/Crushing companies

Contact Information for Business Card

see above

Requirements
Must have
• - logo to remain same along with same font within logo
• - green color to remain same
Nice to have
• as noted above under project description
Should not have

```html
<!DOCTYPE html>
<html lang="en">
<head>
<meta charset="utf-8">
<title>Stonevale Co Business Card</title>
<link rel="stylesheet" href="https://fonts.googleapis.com/css2?family=Arimo:ital,wght@0,400;0,700;1,400&display=swap">
<style>
  :root {
    --backdrop: #9b9b9b;
    --brand-green: #8a8a0b;
    --card-white: #ffffff;
    --ink: #1a1a1a;
    --rule: #a9a9a9;
    --shadow: rgba(0, 0, 0, 0.45);
  }
  * { margin: 0; padding: 0; box-sizing: border-box; }
  html, body {
    width: 1200px;
    height: 900px;
    overflow: hidden;
    background: var(--backdrop);
    font-family: "Arimo", Arial, sans-serif;
  }
  .canvas { position: relative; width: 1200px; height: 900px; }

  .card {
    position: absolute;
    top: 306px;
    width: 439px;
    height: 271px;
    border-radius: 12px;
    box-shadow: 3px 4px 4px var(--shadow);
  }
  .card--front { left: 149px; background: var(--card-white); }
  .card--back { left: 608px; background: var(--brand-green); }

  /* Front: brand block */
  .brand-mark {
    position: absolute;
    left: 97px;
    top: 88px;
    width: 26px;
    height: 26px;
    border-radius: 50%;
    background: var(--brand-green);
  }
  .brand-name {
    position: absolute;
    left: 20px;
    top: 138px;
    width: 200px;
    font-size: 15.5px;
    font-weight: 700;
    color: var(--ink);
    letter-spacing: 0.1px;
    white-space: nowrap;
  }
  .tagline {
    position: absolute;
    left: 27px;
    top: 176px;
    font-size: 13.5px;
    font-style: italic;
    letter-spacing: 1.3px;
    color: var(--brand-green);
    white-space: nowrap;
  }
  .divider {
    position: absolute;
    left: 237px;
    top: 64px;
    width: 1px;
    height: 142px;
    background: var(--rule);
  }

  /* Front: contact block */
  .contact {
    position: absolute;
    left: 258px;
    top: 59px;
    color: var(--ink);
  }
  .contact__name {
    font-size: 17px;
    color: var(--brand-green);
    letter-spacing: 0.3px;
    margin-bottom: 6px;
  }
  .contact__list { list-style: none; }
  .contact__item {
    display: flex;
    align-items: center;
    height: 16px;
    font-size: 12.5px;
  }
  .contact__icon {
    width: 9px;
    height: 9px;
    margin-right: 6px;
    flex: none;
  }
  .contact__address {
    font-style: normal;
    font-size: 12.5px;
    line-height: 16px;
    margin-top: 9px;
    margin-left: 1px;
  }

  /* Back */
  .back-name {
    position: absolute;
    left: 0;
    width: 100%;
    top: 127px;
    padding-left: 180px;
    font-size: 13px;
    font-weight: 700;
    color: var(--card-white);
    letter-spacing: 0.4px;
    white-space: nowrap;
  }
</style>
</head>
<body>
<main class="canvas">

  <section class="card card--front" aria-label="Business card front">
    <span class="brand-mark" aria-hidden="true"></span>
    <p class="brand-name">THE STONEVALE CO.</p>
    <p class="tagline">CRUSHING SOLUTIONS</p>
    <span class="divider" aria-hidden="true"></span>

    <div class="contact">
      <h1 class="contact__name">DEAN MARLOW</h1>
      <ul class="contact__list">
        <li class="contact__item">
          <svg class="contact__icon" viewBox="0 0 10 10" aria-hidden="true"><path fill="var(--brand-green)" d="M0 3.2C0 1.6 2 1 5 1s5 .6 5 2.2V4H7.3V3H2.7v1H0z M2 5h6l1 4H1z"/><circle cx="5" cy="6.8" r="1.1" fill="#fff"/></svg>
          780.555.0148(Direct)
        </li>
        <li class="contact__item">
          <svg class="contact__icon" viewBox="0 0 10 10" aria-hidden="true"><path fill="var(--brand-green)" d="M0 3.2C0 1.6 2 1 5 1s5 .6 5 2.2V4H7.3V3H2.7v1H0z M2 5h6l1 4H1z"/><circle cx="5" cy="6.8" r="1.1" fill="#fff"/></svg>
          780.555.0172
        </li>
        <li class="contact__item">
          <svg class="contact__icon" viewBox="0 0 10 10" aria-hidden="true"><rect x="2" y="0.5" width="6" height="3" fill="var(--brand-green)"/><rect x="0.5" y="3.5" width="9" height="6" rx="1" fill="var(--brand-green)"/><rect x="2.5" y="5.5" width="5" height="2" fill="#fff"/></svg>
          780.555.0193
        </li>
        <li class="contact__item">
          <svg class="contact__icon" viewBox="0 0 10 10" aria-hidden="true"><rect x="0.5" y="2" width="9" height="6.5" fill="var(--brand-green)"/><path d="M0.8 2.3 5 5.8 9.2 2.3" fill="none" stroke="#fff" stroke-width="0.9"/></svg>
          dean@stonevale.ca
        </li>
        <li class="contact__item">
          <svg class="contact__icon" viewBox="0 0 10 10" aria-hidden="true"><circle cx="5" cy="5" r="4.5" fill="var(--brand-green)"/><path d="M3 3.5c1 0 1.5.8 1 1.6-.4.8.5 1.5 1.2 2.6M6.5 2c-.3.8.3 1.5 1.3 1.4" fill="none" stroke="#fff" stroke-width="0.8"/></svg>
          www.stonevale.ca
        </li>
      </ul>
      <address class="contact__address">
        2215-48B Street<br>
        Nisku, Alberta T9E 1K2
      </address>
    </div>
  </section>

  <section class="card card--back" aria-label="Business card back">
    <p class="back-name">THE STONEVALE CO.</p>
  </section>

</main>
</body>
</html>
```